Book cover design for a collection of poetry - The Lanternfield

Book cover and back design need to be moody, nostalgic, reflective, ethereal. Melancholy and other worldly. Cover design should not be time specific to a period or place but if applicable should reflect British landscape. Book cover should be in tones of blue and must include the title and author (THE LANTERNFIELD BY DORIAN WELKBRIDGE). We love the idea of rain, and looking out of a window. See attached designs. A world you are observing but not in.

Industry/Entity Type

Book Publisher

Font styles to use
Serif
Script

Colors
3176b5
3377b5
85acd3
eaf1f7
0792cd
33a6d7
86cae7
ecf7fb
86cfc6

Requirements
Must have
• The colour blue in it, must be melancholy and reflective.
Nice to have
• Rain in the cover.
Should not have
• Any bright colours.

```html
<!DOCTYPE html>
<html lang="en">
<head>
<meta charset="utf-8">
<title>The Lanternfield – Book Cover</title>
<link rel="stylesheet" href="https://fonts.googleapis.com/css2?family=Tinos:wght@400;700&display=swap">
<style>
  :root {
    --page-bg: #e6e9ec;
    --ink-dark: #070d10;
    --teal-deep: #0f2e2f;
    --teal-mid: #1d4a49;
    --title-steel: #86a3b6;
    --title-shade: #2b3d48;
    --text-light: #f2f5f7;
    --curtain: #c8d2d9;
    --window-grey: #5f686c;
    --garden-green: #59634a;
  }
  * { margin: 0; padding: 0; box-sizing: border-box; }
  html, body {
    width: 1200px; height: 800px; overflow: hidden;
    background: var(--page-bg);
  }
  .canvas {
    position: relative; width: 1200px; height: 800px;
    display: flex; align-items: center; justify-content: center;
  }
  .book-wrap {
    display: flex; height: 720px;
    box-shadow: 0 8px 24px rgba(0,0,0,.25);
    font-family: "Tinos", "Times New Roman", serif;
  }

  /* Back cover */
  .back-cover {
    position: relative; width: 475px; height: 100%;
    background:
      radial-gradient(ellipse at 40% 30%, rgba(40,95,92,.55), transparent 60%),
      radial-gradient(ellipse at 55% 70%, rgba(30,80,78,.45), transparent 55%),
      linear-gradient(180deg, var(--teal-deep) 0%, #0b1c1e 55%, var(--ink-dark) 100%);
    color: var(--text-light);
    text-align: center;
    padding: 48px 34px 0;
  }
  .back-title {
    font-weight: 700; font-size: 40px; letter-spacing: 1px;
    color: var(--title-steel);
    text-shadow: 1px 2px 2px var(--title-shade);
    margin-bottom: 70px;
    white-space: nowrap;
  }
  .blurb p {
    font-size: 15.5px; line-height: 1.55;
    margin-bottom: 24px;
  }

  /* Spine */
  .spine {
    width: 50px; height: 100%;
    background: linear-gradient(180deg, #0c1a1c, var(--ink-dark));
    border-left: 1px solid rgba(255,255,255,.08);
    border-right: 1px solid rgba(0,0,0,.6);
    display: flex; flex-direction: column; align-items: center;
    justify-content: space-between; padding: 30px 0;
    color: var(--text-light);
  }
  .spine-text {
    writing-mode: vertical-rl;
    font-size: 16px; letter-spacing: 1px; white-space: nowrap;
  }

  /* Front cover */
  .front-cover {
    position: relative; width: 475px; height: 100%; overflow: hidden;
    background:
      radial-gradient(ellipse at 20% 20%, rgba(38,90,88,.5), transparent 60%),
      linear-gradient(180deg, #0d1f21 0%, var(--ink-dark) 100%);
  }
  .window-scene {
    position: absolute; top: 0; right: 0; bottom: 0; left: 130px;
    background:
      linear-gradient(90deg, rgba(8,16,18,1) 0%, rgba(8,16,18,0) 30%),
      linear-gradient(180deg, rgba(8,16,18,.9) 0%, rgba(8,16,18,0) 22%),
      linear-gradient(90deg, #7d8a90 0%, var(--curtain) 22%, #9ea9ae 38%, var(--window-grey) 46%, #8a8f84 62%, var(--garden-green) 80%, #6b7268 100%);
  }
  .front-title {
    position: absolute; left: 44px; top: 50px; bottom: 40px;
    writing-mode: vertical-rl; transform: rotate(180deg);
    font-size: 50px; letter-spacing: 1px; white-space: nowrap;
    color: var(--title-steel);
    text-shadow: -2px 1px 2px var(--title-shade);
    text-align: right;
  }
  .front-author {
    position: absolute; left: 104px; top: 40px;
    writing-mode: vertical-rl; transform: rotate(180deg);
    font-size: 34px; white-space: nowrap;
    color: var(--text-light);
    height: 360px; text-align: left;
  }
</style>
</head>
<body>
<main class="canvas">
  <div class="book-wrap">

    <section class="back-cover">
      <h2 class="back-title">THE LANTERNFIELD</h2>
      <div class="blurb">
        <p>The Lanternfield is a collection of poems.</p>
        <p>Told in two parts we first meet Arthur, widowed and left alone in his inherited manor, reflecting on his life and his marriage to Alice, whom we meet in part two. Alice is suicidal, pregnant and struggling with life as a wife, until she finds the harbors and falls in love with a fisherman, and her world is changed forever.</p>
        <p>Moving through the 20th century, The Lanternfield interweaves grief, love, mental illness, and ultimately hope.</p>
      </div>
    </section>

    <section class="spine">
      <span class="spine-text">THE LANTERNFIELD</span>
      <span class="spine-text">DORIAN WELKBRIDGE</span>
    </section>

    <section class="front-cover">
      <div class="window-scene" role="img" aria-label="Photograph of a rain-streaked sash window with a pale curtain, looking out onto a red telephone box and a stone wall"></div>
      <h1 class="front-title">THE LANTERNFIELD</h1>
      <p class="front-author">Dorian Welkbridge</p>
    </section>

  </div>
</main>
</body>
</html>
```